Online business manager needs a website

I need a website designed and then coded. I am an online business manager serving a number of different industries providing administrative support to existing small businesses and helping solo practitioners get their new business up and running.

I didn't have a logo formally designed but have been using the attached avatar and wouldn't mind something that incorporated that.

The business doesn't have an official name, so I've just been using my name Lena Pruvost, Online Business Manager or Lena Pruvost, OBM. I've attached two documents that I have made previously for an example of content.

I would prefer the final site be in Wordpress.

Requirements
Must have
• A way to contact me, testimonials, list of services

```html
<!DOCTYPE html>
<html lang="en">
<head>
<meta charset="utf-8">
<title>Lena Pruvost, OBM</title>
<link href="https://fonts.googleapis.com/css2?family=Oswald:wght@400;500;600;700&family=Roboto:wght@400;500;700&family=Open+Sans:wght@400;600&display=swap" rel="stylesheet">
<style>
:root{
  --purple:#583585;
  --purple-deep:#4f2f7a;
  --yellow:#fdb900;
  --ink:#333;
  --grey:#8a8a8a;
  --white:#fff;
}
*{margin:0;padding:0;box-sizing:border-box}
html,body{width:1200px;height:2881px;overflow:hidden;background:var(--white)}
body{position:relative;font-family:'Roboto',Arial,sans-serif;color:var(--ink)}
.backdrop{position:absolute;left:0;top:0;width:1200px;height:2881px}
.abs{position:absolute}
.brand{left:45px;top:28px;display:flex;align-items:center;gap:10px;font-family:'Oswald',sans-serif;font-weight:600;font-size:25px;color:var(--purple);white-space:nowrap}
.brand-dot{width:56px;height:56px;border-radius:50%;background:var(--yellow);flex:none}
.nav{left:344px;top:50px;display:flex;gap:25px;font-family:'Oswald',sans-serif;font-size:15px;letter-spacing:1.5px;color:var(--purple);font-weight:500}
.nav span:last-child{margin-left:5px}
.topbar{left:930px;top:18px;display:flex;align-items:center;gap:9px;color:var(--white);font-family:'Oswald',sans-serif;font-size:14px}
.social{width:28px;height:28px;border-radius:50%;background:var(--white)}
.hero-title{left:48px;top:296px;font-family:'Oswald',sans-serif;font-weight:600;font-size:36px;line-height:46px;color:var(--purple)}
.hero-title .accent{color:var(--yellow);font-size:41px}
.hero-copy{left:48px;top:396px;width:460px;font-size:14px;line-height:19px;color:#333}
.btn{background:var(--purple);color:var(--white);font-family:'Oswald',sans-serif;font-weight:500;font-size:14px;display:flex;align-items:center;justify-content:center}
.hero-btn{left:48px;top:459px;width:129px;height:45px}
.orbit-label{font-family:'Open Sans',sans-serif;font-size:13px;line-height:17px;color:var(--white)}
.orbit-label.active{font-weight:600}
.avatar{left:282px;top:1036px;width:176px;height:148px;border-radius:6px;background:linear-gradient(160deg,#dfe6ea,#9aa3a8)}
.section-title{font-family:'Oswald',sans-serif;font-weight:600;font-size:35px;color:var(--purple)}
.tag{left:698px;top:990px;width:170px;height:46px;background:#4d3a63;color:var(--white);font-family:'Oswald',sans-serif;font-size:18px;display:flex;align-items:center;justify-content:center}
.card-copy{left:716px;top:1307px;width:360px;font-size:14px;line-height:19px}
.learn{left:716px;top:1355px;font-family:'Oswald',sans-serif;font-weight:600;font-size:14px;color:var(--yellow)}
.arrow-box{width:45px;height:45px;border:1.5px solid var(--purple);display:flex;align-items:center;justify-content:center;background:var(--white)}
.vertical-name{left:1108px;top:905px;writing-mode:vertical-rl;font-family:'Oswald',sans-serif;font-weight:700;font-size:40px;letter-spacing:7px;color:#d7d7d7;white-space:nowrap}
.stat{width:200px;text-align:center;color:var(--white)}
.stat b{display:block;font-family:'Oswald',sans-serif;font-weight:600;font-size:66px;line-height:70px}
.stat span{font-size:18px;font-weight:500}
.news-intro{left:220px;top:1817px;width:760px;text-align:center;font-size:16px;line-height:22px;color:#555}
.news-card{width:281px}
.news-img{height:200px}
.news-title{margin-top:14px;font-family:'Oswald',sans-serif;font-weight:400;font-size:17px;line-height:23px;color:#4a4a4a;white-space:nowrap}
.news-card.featured .news-title{color:var(--purple)}
.news-date{margin-top:8px;font-size:11px;color:var(--grey)}
.contact-lead{left:232px;top:2416px;color:var(--white)}
.contact-lead h3{font-family:'Oswald',sans-serif;font-weight:600;font-size:25px;line-height:30px}
.contact-lead p{margin-top:12px;font-size:15px;line-height:19px}
.contact-col{color:var(--white);width:200px}
.contact-col h4{font-size:17px;font-weight:500}
.contact-col p{margin-top:12px;font-size:14px;line-height:20px}
.contact-col .action{margin-top:20px;font-size:15px;font-weight:500}
.foot-brand{left:50px;top:2640px;display:flex;align-items:center;gap:12px;font-family:'Oswald',sans-serif;font-weight:600;font-size:23px;color:var(--purple);white-space:nowrap}
.foot-logo{width:86px;height:70px;background:var(--yellow);border-radius:4px;flex:none}
.foot-links{font-size:15px;line-height:26px;color:var(--purple)}
.follow{left:839px;top:2645px;font-size:14px;color:var(--grey)}
.follow-icons{left:839px;top:2678px;display:flex;gap:7px}
.follow-icons .social{background:var(--purple);width:30px;height:30px}
.disclaimer{left:49px;top:2762px;width:1110px;font-size:11px;line-height:17px;color:#444}
.copyright{left:47px;top:2813px;font-size:13px;color:#444}
</style>
</head>
<body>
<svg class="backdrop" viewBox="0 0 1073 2577" preserveAspectRatio="none" aria-hidden="true">
  <defs>
    <linearGradient id="heroBg" x1="0" y1="0" x2="1" y2="1">
      <stop offset="0" stop-color="#f4f4f3"/><stop offset=".6" stop-color="#ecebe6"/><stop offset="1" stop-color="#cfd2c4"/>
    </linearGradient>
    <linearGradient id="stripBg" x1="0" y1="0" x2="1" y2="0">
      <stop offset="0" stop-color="#573783"/><stop offset="1" stop-color="#4a2f6c"/>
    </linearGradient>
  </defs>
  <rect x="0" y="0" width="1073" height="573" fill="url(#heroBg)"/>
  <polygon points="0,573 455,573 78,1338 0,1338" fill="#fdb900"/>
  <polygon points="750,0 1073,0 1073,661 410,661" fill="#5a3688"/>
  <circle cx="328" cy="1005" r="286" fill="#5f3a87"/>
  <circle cx="328" cy="1005" r="191" fill="#fff" stroke="#777" stroke-width="2" stroke-dasharray="4 3"/>
  <circle cx="328" cy="1005" r="114" fill="none" stroke="#5f3a87" stroke-width="1.5" stroke-dasharray="6 4"/>
  <g fill="#8a8a8a" stroke="#fff" stroke-width="3">
    <circle cx="275" cy="822" r="11"/><circle cx="440" cy="850" r="11"/><circle cx="153" cy="931" r="11"/>
    <circle cx="168" cy="1107" r="11"/><circle cx="298" cy="1194" r="11"/><circle cx="464" cy="1141" r="11"/>
    <circle cx="240" cy="935" r="10"/><circle cx="418" cy="934" r="10"/><circle cx="400" cy="1095" r="10"/>
  </g>
  <circle cx="519" cy="1005" r="12" fill="#fdb900" stroke="#fff" stroke-width="3"/>
  <rect x="0" y="1338" width="1073" height="193" fill="url(#stripBg)"/>
  <rect x="0" y="2100" width="1073" height="205" fill="#573a80"/>
  <line x1="411" y1="2100" x2="411" y2="2305" stroke="#6e559a" stroke-width="1"/>
</svg>

<div class="abs" role="img" aria-label="Portrait photo of the business manager smiling, resting her chin on her hand" style="left:537px;top:97px;width:613px;height:613px;border-radius:50%;border:31px solid var(--yellow);background:radial-gradient(circle at 45% 35%,#e9c9ad,#c9a583 45%,#9f8b7a 75%,#6b5a58)"></div>

<header>
  <div class="abs brand"><span class="brand-dot"></span>LENA PRUVOST, OBM</div>
  <nav class="abs nav"><span>HOME</span><span>ABOUT</span><span>SERVICES</span><span>INDUSTRY NEWS</span><span>CONTACT</span></nav>
  <div class="abs topbar">Call- 1-800-555-0142 <span class="social"></span><span class="social"></span><span class="social"></span></div>
</header>

<section class="hero">
  <h1 class="abs hero-title">EXPERIENCE INCREASED<br><span class="accent">EFFICIENCY &amp; PRODUCTIVITY</span></h1>
  <p class="abs hero-copy">Lorem ipsum dolor sit amet, consectetur adipiscing elit. Donec vulputate hendrerit metus, a sollicitudin enim porta sed.</p>
  <div class="abs btn hero-btn">EXPLORE NOW</div>
</section>

<section class="expertise">
  <div class="abs avatar" role="img" aria-label="Cartoon avatar waving from a laptop screen"></div>
  <span class="abs orbit-label" style="left:223px;top:883px">eCommerce</span>
  <span class="abs orbit-label" style="left:487px;top:896px">Administrative<br>Support</span>
  <span class="abs orbit-label" style="left:72px;top:1051px">List Building</span>
  <span class="abs orbit-label active" style="left:607px;top:1107px">Virtual<br>Assistant</span>
  <span class="abs orbit-label" style="left:108px;top:1257px">Data Entry</span>
  <span class="abs orbit-label" style="left:505px;top:1298px">Writing Services</span>
  <span class="abs orbit-label" style="left:344px;top:1360px">Creative Design<br>Services</span>

  <h2 class="abs section-title" style="left:716px;top:875px">AREAS OF EXPERTISE</h2>
  <div class="abs" role="img" aria-label="Photo of a smiling virtual assistant wearing a headset at her desk" style="left:713px;top:945px;width:356px;height:354px;background:linear-gradient(135deg,#e7e4df,#c9c0b6 50%,#6f8a5a)"></div>
  <div class="abs tag">VIRTUAL ASSISTANT</div>
  <p class="abs card-copy">Lorem ipsum dolor sit amet, consectetur adipiscing elit. Donec vulputate hendrerit metus.</p>
  <span class="abs learn">LEARN MORE</span>
  <div class="abs arrow-box" style="left:970px;top:1391px"><svg width="30" height="14" viewBox="0 0 30 14"><path d="M29 7H2M8 1L2 7l6 6" fill="none" stroke="#666" stroke-width="1.5"/></svg></div>
  <div class="abs arrow-box" style="left:1025px;top:1391px"><svg width="30" height="14" viewBox="0 0 30 14"><path d="M1 7h27M22 1l6 6-6 6" fill="none" stroke="#583585" stroke-width="1.5"/></svg></div>
  <div class="abs vertical-name">LENA PRUVOST, OBM</div>
</section>

<section class="stats">
  <div class="abs stat" style="left:158px;top:1554px"><b>5700</b><span>Successful Projects</span></div>
  <div class="abs stat" style="left:386px;top:1554px"><b>100%</b><span>Data Security</span></div>
  <div class="abs stat" style="left:614px;top:1556px"><b>15</b><span>Years of Experiences</span></div>
  <div class="abs stat" style="left:842px;top:1556px"><b>24/7</b><span>Support</span></div>
</section>

<section class="news">
  <h2 class="abs section-title" style="left:0;width:1200px;text-align:center;top:1772px;font-size:31px">INDUSTRIES NEWS</h2>
  <p class="abs news-intro">Lorem ipsum dolor sit amet, consectetur adipiscing elit. Proin condimentum accumsan dapibus. Integer nec ipsum eget sapien lacinia bibendum non ac turpis.</p>
  <div class="abs arrow-box" style="left:48px;top:2015px;width:51px;height:51px"><svg width="36" height="16" viewBox="0 0 36 16"><path d="M35 8H2M9 1L2 8l7 7" fill="none" stroke="#583585" stroke-width="1.5"/></svg></div>
  <div class="abs arrow-box" style="left:1101px;top:2015px;width:51px;height:51px"><svg width="36" height="16" viewBox="0 0 36 16"><path d="M1 8h33M27 1l7 7-7 7" fill="none" stroke="#583585" stroke-width="1.5"/></svg></div>
  <article class="abs news-card" style="left:155px;top:1897px">
    <div class="news-img" role="img" aria-label="Photo of hands using a tablet showing data dashboards" style="background:linear-gradient(135deg,#e8eaec,#2a3a4a 60%,#1a2530)"></div>
    <h3 class="news-title">LOREM IPSUM DOLOR SIT AMET CONSE CTET<br>UR ADIPISCING ELIT</h3>
    <p class="news-date">Posted on June 11, 2023</p>
  </article>
  <article class="abs news-card featured" style="left:458px;top:1897px">
    <div class="news-img" role="img" aria-label="Illustration of a glowing cloud server" style="background:radial-gradient(circle at 50% 40%,#2f7fa8,#1b2a48 55%,#2a1a3a)"></div>
    <h3 class="news-title">LOREM IPSUM DOLOR SIT AMET CONSE CTET<br>UR ADIPISCING ELIT</h3>
    <p class="news-date">Posted on June 11, 2023</p>
  </article>
  <article class="abs news-card" style="left:761px;top:1897px">
    <div class="news-img" role="img" aria-label="Photo of a small shopping cart beside a laptop" style="background:linear-gradient(135deg,#c9a06a,#e6e2dc 50%,#b9bcc4)"></div>
    <h3 class="news-title">LOREM IPSUM DOLOR SIT AMET CONSE CTET<br>UR ADIPISCING ELIT</h3>
    <p class="news-date">Posted on June 11, 2023</p>
  </article>
  <div class="abs btn" style="left:502px;top:2219px;width:196px;height:48px">VIEW ALL LATEST NEWS</div>
</section>

<section class="contact">
  <div class="abs contact-lead"><h3>HOW CAN<br>HELP YOU?</h3><p>Connect with Lena Pruvost<br>to get started.</p></div>
  <div class="abs contact-col" style="left:536px;top:2405px"><h4>Call Us</h4><p>Give us a call – we'd love to hear from you.</p><p class="action">1 800 555 0142</p></div>
  <div class="abs contact-col" style="left:763px;top:2405px"><h4>Email Us</h4><p>Fill out a short form and hear we'll get right back to you.</p><p class="action">SEND US A NOTE ›</p></div>
</section>

<footer>
  <div class="abs foot-brand"><span class="foot-logo"></span>LENA PRUVOST, OBM</div>
  <div class="abs foot-links" style="left:384px;top:2642px">Home<br>About<br>Services</div>
  <div class="abs foot-links" style="left:611px;top:2642px">Industry News<br>Contact</div>
  <div class="abs follow">Follow Us</div>
  <div class="abs follow-icons"><span class="social"></span><span class="social"></span><span class="social"></span></div>
  <p class="abs disclaimer">Disclaimers: Lorem ipsum dolor sit amet, consectetur adipiscing elit. Donec vulputate hendrerit metus, a sollicitudin enim porta sed. Mauris venenatis pellentesque finibus. Duis faucibus mauris at ante dictum sollicitudin. Cras pretium, leo eu porta rhoncus, nulla ipsum commodo dolor, ut euismod lacus arcu sit amet enim.</p>
  <p class="abs copyright">Copyright © 2023 Lena Pruvost, OBM</p>
</footer>
</body>
</html>
```